Dental office stationary (letterhead, envelopes), business cards, presentation folders

Nothing too dental outside of the logo. I will need all stationary, presentation folders, business cards. Would prefer to stay in the colors of the logo

Gordon Pellham, DDS
Brightwell Dental Implant Center
555-555-0187
info@brightwelldental-example.com
3871 NW Corbin Rd Unit B
Larkhaven, FL 39990

Also need appointment date and time
And cancellation policy
I want it to say “kindly ask for
A 48hr cancellation policy to avoid incurring a cancellation fee”

Industry/Entity Type

Dental

Colors
0054AA
0677BA
7BADD7
CADEEF
E8F1F8

Requirements
Must have
• Name of your office, name of doctor, address, phone number
Should not have
• Too much tooth/dental. Only the tooth in logo

```html
<!DOCTYPE html>
<html lang="en">
<head>
<meta charset="utf-8">
<title>Brightwell Dental Implant Center – Stationery</title>
<link href="https://fonts.googleapis.com/css2?family=Montserrat:wght@400;500;600;700&display=swap" rel="stylesheet">
<style>
  :root{
    --bg:#e3e4e6;
    --header:#3a3a3c;
    --blue-light:#22c3f2;
    --blue:#1a9ad6;
    --blue-deep:#1e86cb;
    --teal:#0fb9a0;
    --ink:#333;
    --muted:#6f6f6f;
    --label:#555;
    --white:#fff;
    --shadow:2px 3px 5px rgba(0,0,0,.35);
  }
  *{box-sizing:border-box;margin:0;padding:0}
  html,body{width:757px;height:1200px;overflow:hidden}
  body{background:var(--bg);font-family:"Montserrat",sans-serif;color:var(--ink);position:relative}
  .header{position:absolute;left:0;top:0;width:757px;height:76px;background:var(--header);display:flex;align-items:center;justify-content:center}
  .abs{position:absolute}
  .label{position:absolute;font-size:5px;color:var(--label)}
  .sheet{position:absolute;background:var(--white);box-shadow:var(--shadow);overflow:hidden}
  .band{position:absolute;left:0;bottom:0;width:100%;height:3px;
    background:linear-gradient(90deg,var(--blue-light),var(--blue-deep) 85%,var(--teal) 85%)}
  .gradient{background:linear-gradient(90deg,var(--blue-light),var(--blue-deep))}

  .logo{display:flex;align-items:center;gap:4px;font-weight:600;color:var(--blue);letter-spacing:.02em;white-space:nowrap}
  .logo .dot{border-radius:50%;background:currentColor;flex:none}
  .logo.on-dark{color:var(--white)}

  .contact{list-style:none;font-size:3.6px;color:var(--ink)}
  .contact li{display:flex;align-items:flex-start;gap:3px;margin-bottom:4px;line-height:1.2;white-space:nowrap}
  .contact svg{flex:none}

  .card-name{position:absolute;right:11px;top:17px;text-align:right}
  .card-name strong{display:block;font-size:5px;font-weight:600;color:var(--blue);letter-spacing:.02em}
  .card-name span{font-size:3.4px;color:var(--muted);margin-top:1px;padding-bottom:3px;border-bottom:.6px solid var(--ink);display:inline-block}

  .letter{font-size:5px;color:var(--muted)}
  .letter .recipient{position:absolute;left:26px;top:101px}
  .letter .recipient h2{font-size:8.5px;font-weight:600;color:var(--blue);margin-bottom:6px}
  .letter .recipient p{font-size:4.8px;line-height:1.5;margin-bottom:1.5px}
  .letter .date{position:absolute;right:25px;top:141px;font-size:5.6px}
  .letter .body{position:absolute;left:26px;top:154px;width:237px;font-size:5.2px;line-height:1.65;text-align:justify}
  .letter .body p{margin-bottom:8px}
  .letter .sign-name{position:absolute;left:26px;top:275px;font-size:8px;color:var(--ink)}
  .letter .signature{position:absolute;left:26px;top:291px;width:48px;height:16px;background:#ececec;border-radius:2px}

  .folder-panel{position:absolute;top:620px;width:300px;height:401px}
  .pocket{position:absolute;background:var(--teal)}
</style>
</head>
<body>

<header class="header">
  <div class="logo" style="font-size:17px"><span class="dot" style="width:6px;height:6px"></span>BRIGHTWELL</div>
</header>

<!-- Business card front -->
<span class="label" style="left:49px;top:101px">Bcard Front</span>
<section class="sheet business-card-front" style="left:49px;top:110px;width:161px;height:96px">
  <div class="logo abs" style="left:11px;top:19px;font-size:8px"><span class="dot" style="width:3px;height:3px"></span>BRIGHTWELL</div>
  <div class="card-name"><strong>GORDON PELLHAM, DDS</strong><span>Brightwell Dental Implant Center</span></div>
  <ul class="contact abs" style="left:11px;top:60px">
    <li><svg width="5" height="5" viewBox="0 0 10 10"><rect width="10" height="10" rx="2" fill="#1a9ad6"/><circle cx="5" cy="4.5" r="2" fill="#fff"/></svg><span>3871 NW Corbin Rd Unit B<br>Larkhaven, FL 39990</span></li>
    <li><svg width="5" height="5" viewBox="0 0 10 10"><rect width="10" height="10" rx="2" fill="#0fb9a0"/><path d="M3 2.5l1.2 1.4-.7 1a4 4 0 002 2l1-.7 1.4 1.2-.8 1.1C4.8 8.3 2 5.5 1.9 3.3z" fill="#fff"/></svg><span>555-555-0187</span></li>
    <li><svg width="5" height="5" viewBox="0 0 10 10"><rect width="10" height="10" rx="2" fill="#1a9ad6"/><rect x="2" y="3" width="6" height="4" fill="none" stroke="#fff" stroke-width=".8"/></svg><span>info@brightwelldental-example.com</span></li>
  </ul>
  <div class="band"></div>
</section>

<!-- Business card back -->
<span class="label" style="left:227px;top:101px">Bcard Back</span>
<section class="sheet business-card-back gradient" style="left:227px;top:110px;width:163px;height:97px;display:flex;align-items:center;justify-content:center">
  <div class="logo on-dark" style="font-size:11px"><span class="dot" style="width:4px;height:4px"></span>BRIGHTWELL</div>
</section>

<!-- Envelope front -->
<span class="label" style="left:49px;top:224px">Envelope</span>
<section class="sheet envelope-front" style="left:49px;top:236px;width:323px;height:162px">
  <div class="logo abs" style="left:11px;top:17px;font-size:9.5px"><span class="dot" style="width:3.5px;height:3.5px"></span>BRIGHTWELL</div>
  <ul class="contact abs" style="left:11px;top:148px">
    <li><svg width="5" height="5" viewBox="0 0 10 10"><rect width="10" height="10" rx="2" fill="#1a9ad6"/><circle cx="5" cy="4.5" r="2" fill="#fff"/></svg><span>3871 NW Corbin Rd Unit B Larkhaven, FL 39990</span></li>
  </ul>
  <div class="band"></div>
</section>

<!-- Envelope back -->
<section class="sheet envelope-back" style="left:47px;top:421px;width:325px;height:163px">
  <svg class="abs" style="left:0;top:0" width="325" height="40" viewBox="0 0 325 40">
    <defs><linearGradient id="flap" x1="0" x2="1"><stop offset="0" stop-color="#22c3f2"/><stop offset="1" stop-color="#1e86cb"/></linearGradient></defs>
    <path d="M0 0H325L316 33Q314 39 307 39H18Q11 39 9 33Z" fill="url(#flap)"/>
  </svg>
  <div class="logo on-dark abs" style="left:50%;top:15px;transform:translateX(-50%);font-size:7.5px"><span class="dot" style="width:3px;height:3px"></span>BRIGHTWELL</div>
</section>

<!-- Letterhead -->
<span class="label" style="left:414px;top:101px">LetterHead</span>
<section class="sheet letter" style="left:414px;top:110px;width:288px;height:404px">
  <div class="logo abs" style="left:25px;top:32px;font-size:11px"><span class="dot" style="width:4px;height:4px"></span>BRIGHTWELL</div>
  <ul class="contact abs" style="left:206px;top:18px">
    <li><svg width="5" height="5" viewBox="0 0 10 10"><rect width="10" height="10" rx="2" fill="#1a9ad6"/><circle cx="5" cy="4.5" r="2" fill="#fff"/></svg><span>3871 NW Corbin Rd Unit B<br>Larkhaven, FL 39990</span></li>
    <li><svg width="5" height="5" viewBox="0 0 10 10"><rect width="10" height="10" rx="2" fill="#0fb9a0"/><path d="M3 2.5l1.2 1.4-.7 1a4 4 0 002 2l1-.7 1.4 1.2-.8 1.1C4.8 8.3 2 5.5 1.9 3.3z" fill="#fff"/></svg><span>555-555-0187</span></li>
    <li><svg width="5" height="5" viewBox="0 0 10 10"><rect width="10" height="10" rx="2" fill="#0fb9a0"/><rect x="2" y="3" width="6" height="4" fill="none" stroke="#fff" stroke-width=".8"/></svg><span>info@brightwelldental-example.com</span></li>
  </ul>
  <div class="recipient">
    <h2>Mr. Dale Renner</h2>
    <p>0123-456-789</p>
    <p>info@youremailaddress.com</p>
    <p style="line-height:1.25">1234 City Your Ln. Suite<br>123 Dallas, TX 0000</p>
  </div>
  <div class="date">12 December, 2024</div>
  <div class="body">
    <p>Lorem ipsum dolor sit amet, consectetuer adipiscing elit, sed diam nonummy nibh euismod tincidunt ut laoreet dolore magna aliquam erat volutpat. Ut wisi enim ad minim veniam, quis nostrud exerci tation ullamcorper suscipit lobortis nisl ut aliquip ex ea commodo consequat. Duis autem vel eum iriure dolor in hendrerit in vulputate velit esse molestie consequat, vel illum dolore eu feugiat nulla facilisis at vero eros et accumsan et iusto odio dignissim qui blandit praesent luptatum zzril delenit augue duis dolore te feugait nulla facilisi.</p>
    <p>Lorem ipsum dolor sit amet, cons ectetuer adipiscing elit, sed diam nonummy nibh euismod tincidunt ut laoreet dolore magna aliquam erat volutpat. Ut wisi enim ad minim veniam, quis nostrud exerci tation ullamcorper suscipit lobortis nisl ut aliquip ex ea commodo consequat.</p>
  </div>
  <div class="sign-name">Mr. Dale Renner</div>
  <div class="signature" role="img" aria-label="Handwritten signature"></div>
  <div class="band"></div>
</section>

<!-- Presentation folder -->
<div class="pocket" style="left:50px;top:915px;width:26px;height:100px;clip-path:polygon(0 10%,100% 0,100% 100%,0 90%)"></div>
<div class="pocket" style="left:674px;top:915px;width:26px;height:100px;clip-path:polygon(0 0,100% 10%,100% 90%,0 100%)"></div>

<section class="folder-panel gradient" style="left:75px">
  <div class="logo on-dark abs" style="left:60px;top:207px;font-size:10.5px"><span class="dot" style="width:4px;height:4px"></span>BRIGHTWELL</div>
  <ul class="contact abs" style="left:154px;top:182px;font-size:6px;color:var(--white)">
    <li><svg width="8" height="8" viewBox="0 0 10 10"><rect width="10" height="10" rx="2" fill="#fff"/><circle cx="5" cy="4.5" r="2" fill="#1a9ad6"/></svg><span>3871 NW Corbin Rd Unit B<br>Larkhaven, FL 39990</span></li>
    <li><svg width="8" height="8" viewBox="0 0 10 10"><rect width="10" height="10" rx="2" fill="#fff"/><path d="M3 2.5l1.2 1.4-.7 1a4 4 0 002 2l1-.7 1.4 1.2-.8 1.1C4.8 8.3 2 5.5 1.9 3.3z" fill="#1a9ad6"/></svg><span>555-555-0187</span></li>
    <li><svg width="8" height="8" viewBox="0 0 10 10"><rect width="10" height="10" rx="2" fill="#fff"/><rect x="2" y="3" width="6" height="4" fill="none" stroke="#1a9ad6" stroke-width=".8"/></svg><span>info@brightwelldental-example.com</span></li>
  </ul>
</section>

<section class="folder-panel" style="left:375px;background:var(--white);box-shadow:var(--shadow)">
  <div class="logo abs" style="left:50%;top:85px;transform:translateX(-50%);font-size:24px"><span class="dot" style="width:8px;height:8px"></span>BRIGHTWELL</div>
  <div class="band" style="height:10px"></div>
</section>

<div class="pocket" style="left:75px;top:1020px;width:300px;height:133px;clip-path:polygon(0 0,100% 0,96% 100%,0 100%)"></div>
<div class="pocket" style="left:375px;top:1020px;width:300px;height:133px;clip-path:polygon(0 0,100% 0,100% 100%,9% 100%)"></div>

</body>
</html>
```